exquisite label design for foam cleanser

Kindly invite you to design bottle label (102 mm*64 mm) for our product, a kind of foam cleanser for wearable aligners. The color of bottle and liquid inside are both clear, but the foam pump is white. You could download the pic of bottle among the uploaded files. I have no KV of our website or posters to supply you, except the logo file attached. Content on the label is attached too. Please check it. I wish the label would make our product look high-end and reliable. And it would be better if you could give some advice on paper material and special requirements for printing, related to your design. I value the texture of label too, because I think that stands for the quality of products. No color limitation for the use of our logo, and please ignore the Chinese characters in our logo, they are not in our plan.
Target Market(s)
16-35 female, orthodontic patients.
Colors
Designer to choose colors to be used in the design.
Look and feel

```html
<!DOCTYPE html>
<html lang="en">
<head>
<meta charset="utf-8">
<title>Clarelle Aligner Cleaning Foam – Label</title>
<link href="https://fonts.googleapis.com/css2?family=Montserrat:wght@400;500;700&family=Noto+Sans+TC:wght@400&display=swap" rel="stylesheet">
<style>
  :root {
    --canvas-bg: #f6f6f6;
    --label-bg: #f4f4f4;
    --label-edge: #e4e4e4;
    --brand-blue: #4aa6d6;
    --sub-blue: #3a8cc6;
    --claim-light: #5cbbe0;
    --claim-mid: #2f7fc0;
    --claim-deep: #2c3f9e;
    --claim-text: #ffffff;
    --body-text: #333333;
  }
  html, body {
    margin: 0;
    padding: 0;
    width: 1200px;
    height: 1200px;
    overflow: hidden;
    background: var(--canvas-bg);
  }
  .canvas {
    position: relative;
    width: 1200px;
    height: 1200px;
  }
  .label {
    position: absolute;
    left: 300px;
    top: 66px;
    width: 600px;
    height: 1068px;
    background: linear-gradient(90deg, var(--label-edge) 0%, var(--label-bg) 12%, #fafafa 50%, var(--label-bg) 88%, var(--label-edge) 100%);
    font-family: "Montserrat", sans-serif;
    text-align: center;
  }
  .brand-name {
    position: absolute;
    left: 0; right: 0;
    top: 118px;
    margin: 0;
    font-weight: 700;
    font-size: 92px;
    line-height: 1;
    color: var(--brand-blue);
    letter-spacing: 2px;
  }
  .product-type {
    position: absolute;
    left: 0; right: 0;
    top: 278px;
    margin: 0;
    font-family: "Noto Sans TC", sans-serif;
    font-weight: 400;
    font-size: 42px;
    line-height: 1.2;
    color: var(--sub-blue);
    letter-spacing: 1px;
  }
  .claim-panel {
    position: absolute;
    left: 68px;
    top: 422px;
    width: 465px;
    height: 317px;
    background: linear-gradient(120deg, var(--claim-light) 0%, var(--claim-mid) 50%, var(--claim-deep) 100%);
    color: var(--claim-text);
    display: flex;
    flex-direction: column;
    align-items: center;
    justify-content: center;
    line-height: 1;
  }
  .claim-small { font-size: 44px; font-weight: 400; }
  .claim-large { font-size: 64px; font-weight: 400; }
  .claim-amp { font-size: 36px; margin: 8px 0 10px; }
  .flavor {
    position: absolute;
    left: 0; right: 0;
    top: 850px;
    margin: 0;
    font-size: 38px;
    font-weight: 500;
    color: var(--body-text);
  }
  .volume {
    position: absolute;
    left: 0; right: 0;
    top: 990px;
    margin: 0;
    font-size: 32px;
    font-weight: 400;
    color: var(--body-text);
    letter-spacing: 1px;
  }
</style>
</head>
<body>
  <main class="canvas">
    <section class="label">
      <h1 class="brand-name">Clarelle</h1>
      <p class="product-type" lang="zh-Hant">隱形牙套清潔泡沫</p>
      <div class="claim-panel">
        <span class="claim-small">DEEP</span>
        <span class="claim-large">CLEANING</span>
        <span class="claim-amp">&amp;</span>
        <span class="claim-small">LASTING</span>
        <span class="claim-large">FRESHNESS</span>
      </div>
      <p class="flavor">Mint Flavor</p>
      <p class="volume">1.69 Fl Oz / 50ml</p>
    </section>
  </main>
</body>
</html>
```